Design a few pages of a luxury magazine for the Prestige Gastschule Paris

We need a luxury design for our magazine. See the inDesign pages of the current version attached (zip).

Please work primarily on the first double page (Imaginez l'élégance future) that contains only one photo with legend, a title and the text both in French and English. It must be made clear that the text is the same in two different languages (it is not clear enough here).

You can also work on the other two double pages selected. Feedback will be provided and the 10 best pages will be submitted to a vote at the end of the project timespan.

The most important is a classy and luxury design, this will be printed on expensive paper.

See the full brochure here: https://www.prestigegastschule.example/brochure/#page=4

Target Market(s)

Students and parents

Industry/Entity Type

Education

Colors

Designer to choose colors to be used in the design.

Requirements
Must have
• Luxury magazine layout, see:
• https://www.findlyseek.example/search?q=luxury+magazine+layout
Nice to have
• The color of the cover that should be used for blue and grey is #393d49.
• Our font for serif titles (from the logo) is Adobe TRAJAN.
Should not have
• flashy colors

```html
<!DOCTYPE html>
<html lang="fr">
<head>
<meta charset="utf-8">
<title>Prestige Gastschule Paris — Imaginez l'élégance future</title>
<link href="https://fonts.googleapis.com/css2?family=Playfair+Display:wght@400;700&family=Inter:wght@400&display=swap" rel="stylesheet">
<style>
  :root {
    --backdrop: #e4e4e4;
    --paper: #f1f1f1;
    --paper-shade: #e2e2e2;
    --slate: #434b4f;
    --slate-deep: #0f1a20;
    --ink: #1d1d1d;
    --ink-light: #f4f4f4;
    --photo-warm: #a88a5c;
    --photo-dark: #3b3428;
    --photo-green: #6f7a3a;
  }
  * { margin: 0; padding: 0; box-sizing: border-box; }
  html, body { width: 1200px; height: 1200px; overflow: hidden; background: var(--backdrop); }
  .spread {
    position: absolute; left: 110px; top: 300px;
    width: 980px; height: 600px;
    display: flex;
    box-shadow: 0 20px 40px rgba(0,0,0,0.18);
  }
  .page { position: relative; width: 490px; height: 600px; }
  .page--fr {
    background: linear-gradient(to right, var(--paper) 80%, var(--paper-shade));
    color: var(--ink);
  }
  .page--en {
    background: linear-gradient(to right, var(--slate-deep) 0%, var(--slate) 35%, var(--slate) 100%);
    color: var(--ink-light);
  }
  .feature-photo {
    position: absolute; top: 24px; left: 330px;
    width: 320px; height: 300px;
    border: 6px solid #f7f7f7;
    z-index: 2;
  }
  .article {
    position: absolute; bottom: 46px; width: 370px;
  }
  .page--fr .article { left: 48px; }
  .page--en .article { right: 48px; text-align: right; }
  .article__title {
    font-family: "Playfair Display", serif;
    line-height: 1.05; margin-bottom: 16px;
  }
  .article__title strong { display: block; font-weight: 700; font-size: 26px; }
  .article__title span { display: block; font-weight: 400; font-size: 25px; }
  .article__body {
    font-family: "Inter", sans-serif;
    font-size: 8.6px; line-height: 1.45;
    text-align: justify; text-align-last: left;
  }
  .page--en .article__body { text-align-last: right; }
  .article__body p + p { margin-top: 6px; }
</style>
</head>
<body>
  <div class="spread">
    <section class="page page--fr" lang="fr">
      <div class="article">
        <h1 class="article__title"><strong>Imaginez</strong><span>l'élégance future</span></h1>
        <div class="article__body">
          <p>Depuis sa création il y a 30 ans, notre école garde le même objectif : que chaque étudiant acquière les compétences et développe les talents essentiels pour briller dans l'univers du luxe. Première école dédiée à l'hôtellerie de luxe, la Prestige Gastschule délivre un Bachelor et un Master of Science in International Tourism and Hospitality Management, deux grades universitaires anglais. Cette combinaison du luxe à la française et du management anglosaxon donne toutes les clés à nos étudiants pour s'assurer une place privilégiée dans l'univers du luxe en France et à l'international. Grâce à l'excellence académique de nos programmes, la dimension internationale de nos formations et l'immersion professionnelle à travers des stages dans les plus prestigieux hôtels du monde, tous nos diplômés sont assurés de faire carrière dans le secteur de leur choix à un poste stratégique. La moitié d'entre eux signent un CDI avant même la fin de leur dernier stage.</p>
        </div>
      </div>
    </section>
    <section class="page page--en" lang="en">
      <div class="article">
        <h2 class="article__title"><strong>Invent</strong><span>the luxury of tommorow</span></h2>
        <div class="article__body">
          <p>Since its foundation 30 years ago, our school has had only one object: that each student acquires the skills and develops the essential talents they require to shine within the luxury sector. The Prestige Gastschule is the first Higher Education establishment dedicated to luxury hotel training: we offer a Bachelor's and a Master's degree in International Tourism and Hospitality Management. This combination of French-style luxury and Anglo-Saxon management gives our students the key elements they need to ensure a privileged position within the luxury industry both in France and internationally. The academic excellence of our programmes, the international dimension of our training and our professional work placements at the most prestigious hotels in the world all ensure that our graduates are certain to secure a career in a strategic role in the luxury sector. Half of our students sign a permanent contract before they even finish their final work placement.</p>
        </div>
      </div>
    </section>
    <svg class="feature-photo" role="img" aria-label="Photograph of three school directors in dark suits in an ornate hotel lounge with a green sofa" viewBox="0 0 320 300" preserveAspectRatio="none">
      <defs>
        <linearGradient id="lounge" x1="0" y1="0" x2="0" y2="1">
          <stop offset="0" stop-color="var(--photo-dark)"/>
          <stop offset="0.55" stop-color="var(--photo-warm)"/>
          <stop offset="1" stop-color="#c9ad80"/>
        </linearGradient>
      </defs>
      <rect width="320" height="300" fill="url(#lounge)"/>
      <rect x="60" y="170" width="200" height="60" fill="var(--photo-green)" opacity="0.45"/>
    </svg>
  </div>
</body>
</html>
```